Fitness competition business needs a card design

I need a professional business card design using my logo. The card will be horizontal with rounded edges.

Target Market(s)

Female fitness competitors

Industry/Entity Type

Fitness

Contact Information for Business Card

Rose-Lynn Darby
Owner
stagevarno.com
555.301.2187
info@stagevarno.com

Font styles to use
Serif

Colors

Designer to choose colors to be used in the design.

Requirements
Must have
• On the back please add the following:
• Figure
• Bikini
• Physique
• Fitness
Nice to have
• Looking for a very sleek design, contemporary and easy to read.
Should not have
• Should not be difficult to read or be too busy

```html
<!DOCTYPE html>
<html lang="en">
<head>
<meta charset="utf-8">
<title>Stage Varno – Business Card</title>
<link rel="stylesheet" href="https://fonts.googleapis.com/css2?family=Roboto:wght@400;500;700;900&family=Black+Ops+One&display=swap">
<style>
  :root {
    --bg: #d4e7ec;
    --red: #e8232a;
    --grey: #5a5a5c;
    --grey-dark: #3c3c3e;
    --white: #ffffff;
    --ink: #2a2a2a;
  }
  * { box-sizing: border-box; margin: 0; padding: 0; }
  html, body {
    width: 1200px; height: 900px; overflow: hidden;
    background: var(--bg);
    font-family: "Roboto", Arial, sans-serif;
  }
  .canvas { position: relative; width: 1200px; height: 900px; }

  .card {
    position: absolute;
    width: 600px; height: 343px;
    border-radius: 22px;
    overflow: hidden;
    box-shadow: 0 6px 16px rgba(0,0,0,0.22);
  }

  /* ---------- Back side ---------- */
  .card-back { left: 60px; top: 70px; background: var(--red); }
  .brand {
    position: absolute; left: 0; right: 0;
    text-align: center;
    font-weight: 900;
    letter-spacing: 3px;
    text-transform: uppercase;
    white-space: nowrap;
  }
  .card-back .brand { top: 86px; font-size: 58px; color: var(--white); }
  .brand-mark {
    display: inline-block; width: 18px; height: 18px;
    margin-right: 14px; vertical-align: middle;
    position: relative; top: -6px;
  }
  .card-back .brand-mark { background: var(--grey); }
  .rule-pair { position: absolute; }
  .rule-pair span { display: block; height: 4px; background: var(--grey); }
  .rule-pair span + span { margin-top: 5px; }
  .card-back .rule-pair { left: 110px; width: 380px; top: 170px; }

  .categories {
    position: absolute; left: 40px; right: 40px; top: 220px;
    display: flex; justify-content: space-between;
    font-family: "Black Ops One", "Roboto", sans-serif;
    font-size: 22px; color: var(--white);
    letter-spacing: 1px; text-transform: uppercase;
  }
  .card-back .site {
    position: absolute; left: 0; right: 0; top: 282px;
    text-align: center; color: var(--white);
    font-size: 17px; letter-spacing: 0.5px;
  }

  /* ---------- Front side ---------- */
  .card-front { left: 540px; top: 480px; background: var(--white); }
  .red-panel {
    position: absolute; inset: 0;
    background: var(--red);
    clip-path: polygon(43% 0, 100% 0, 100% 100%, 58% 100%);
  }
  .panel-edge {
    position: absolute; inset: 0;
    filter: drop-shadow(-4px 0 6px rgba(0,0,0,0.25));
  }
  .name-ribbon {
    position: absolute; left: 232px; top: 34px;
    width: 248px; height: 66px;
    background: var(--grey);
    color: var(--white);
    text-align: center;
    padding-top: 12px;
  }
  .name-ribbon .person { font-size: 22px; font-weight: 500; white-space: nowrap; }
  .name-ribbon .role { font-size: 11px; letter-spacing: 1px; margin-top: 3px; text-transform: uppercase; }
  .ribbon-fold { position: absolute; left: 232px; top: 100px; }

  .card-front .brand {
    top: 128px; left: 36px; right: auto;
    text-align: left;
    font-size: 30px; line-height: 36px; color: var(--red); letter-spacing: 1.5px;
  }
  .card-front .brand-mark { width: 12px; height: 12px; margin-right: 10px; top: -3px; background: var(--grey); }
  .card-front .rule-pair { left: 40px; width: 236px; top: 172px; }
  .card-front .rule-pair span { height: 3px; }

  .contacts { position: absolute; left: 46px; top: 224px; list-style: none; }
  .contacts li {
    display: flex; align-items: center; gap: 12px;
    font-size: 17px; color: var(--ink);
    height: 30px; white-space: nowrap;
  }
  .contacts .icon {
    width: 22px; height: 22px; background: var(--red);
    display: flex; align-items: center; justify-content: center;
  }
  .address {
    position: absolute; right: 46px; bottom: 50px;
    width: 200px; text-align: center;
    color: var(--white); font-size: 15px; line-height: 1.35;
  }
  .address svg { display: block; margin: 0 auto 8px; }
</style>
</head>
<body>
<div class="canvas">

  <section class="card card-back" aria-label="Card back">
    <div class="brand"><span class="brand-mark"></span>Stage Varno</div>
    <div class="rule-pair"><span></span><span></span></div>
    <div class="categories">
      <span>Figure</span><span>Bikini</span><span>Physique</span><span>Fitness</span>
    </div>
    <div class="site">stagevarno.com</div>
  </section>

  <section class="card card-front" aria-label="Card front">
    <div class="panel-edge"><div class="red-panel"></div></div>

    <svg class="ribbon-fold" width="28" height="18" viewBox="0 0 28 18" aria-hidden="true">
      <polygon points="0,0 28,0 28,18" fill="var(--grey-dark)"/>
    </svg>
    <div class="name-ribbon">
      <div class="person">Rose-Lynn Darby</div>
      <div class="role">Owner</div>
    </div>

    <div class="brand"><span class="brand-mark"></span>Stage Varno</div>
    <div class="rule-pair"><span></span><span></span></div>

    <ul class="contacts">
      <li>
        <span class="icon">
          <svg width="14" height="14" viewBox="0 0 24 24" aria-hidden="true"><path fill="#fff" d="M6.6 10.8a15 15 0 0 0 6.6 6.6l2.2-2.2c.3-.3.7-.4 1-.2 1.1.4 2.3.6 3.6.6.6 0 1 .4 1 1V20c0 .6-.4 1-1 1C10.6 21 3 13.4 3 4c0-.6.4-1 1-1h3.5c.6 0 1 .4 1 1 0 1.3.2 2.5.6 3.6.1.3 0 .7-.2 1z"/></svg>
        </span>555.301.2187
      </li>
      <li>
        <span class="icon">
          <svg width="14" height="14" viewBox="0 0 24 24" aria-hidden="true"><rect x="3" y="6" width="18" height="12" fill="none" stroke="#fff" stroke-width="2"/><path d="M3 6l9 7 9-7" fill="none" stroke="#fff" stroke-width="2"/></svg>
        </span>info@stagevarno.com
      </li>
      <li>
        <span class="icon">
          <svg width="14" height="14" viewBox="0 0 24 24" aria-hidden="true"><circle cx="12" cy="12" r="9" fill="none" stroke="#fff" stroke-width="2"/><path d="M3 12h18M12 3c3 3 3 15 0 18M12 3c-3 3-3 15 0 18" fill="none" stroke="#fff" stroke-width="1.6"/></svg>
        </span>stagevarno.com
      </li>
    </ul>

    <div class="address">
      <svg width="14" height="18" viewBox="0 0 24 30" aria-hidden="true"><path fill="#fff" d="M12 0C5.4 0 0 5.3 0 11.8 0 20.6 12 30 12 30s12-9.4 12-18.2C24 5.3 18.6 0 12 0zm0 16a4.3 4.3 0 1 1 0-8.6 4.3 4.3 0 0 1 0 8.6z"/></svg>
      48 Harlow Lane<br>Brookfield, ABC 123
    </div>
  </section>

</div>
</body>
</html>
```